Lumora Fabrix
A technical textile company
Lumora Fabrix -
Creative Brief
Professional
Ravi Kapoorji
Business Manager
117, Neel Kamal Residency Chandan Path , Moti Nagar Jaipur - 302049 Rajasthan , India
ravi.kapoorji@lumora-fabrix.example
www.lumora-fabrix.example
Skype : ravikelmora.. Also want - letter head - envelope - power point slide ( both first and regular pages) designs .
Address has to go in the back 117, Neel Kamal Residency Chandan Path , Moti Nagar Jaipur - 302049 Rajasthan , India

```html
<!DOCTYPE html>
<html lang="en">
<head>
<meta charset="utf-8">
<title>Lumora Fabrix – Business Card</title>
<link rel="stylesheet" href="https://fonts.googleapis.com/css2?family=Roboto:wght@400;500;700&display=swap">
<style>
  :root {
    --page: #ffffff;
    --ink: #2b2b2b;
    --brand-blue: #1b5a8c;
    --band-blue: #1d6a96;
    --band-deep: #12496f;
    --accent-orange: #f07c1e;
    --divider: #b9c3cc;
    --back-light: #2f8cc4;
    --back-dark: #0f4b78;
    --white: #ffffff;
  }
  * { margin: 0; padding: 0; box-sizing: border-box; }
  html, body {
    width: 1200px; height: 413px; overflow: hidden;
    background: var(--page);
    font-family: "Roboto", Arial, sans-serif;
  }
  .canvas { position: relative; width: 1200px; height: 413px; }

  .card {
    position: absolute; top: 50px; height: 310px;
    border-radius: 16px; overflow: hidden;
    box-shadow: 0 3px 8px rgba(0,0,0,0.25);
  }

  /* Front */
  .card-front { left: 62px; width: 542px; background: var(--page); }
  .front-brand {
    position: absolute; left: 0; top: 0; width: 262px; height: 240px;
    display: flex; align-items: center; justify-content: center; gap: 10px;
  }
  .brand-dot { width: 22px; height: 22px; border-radius: 50%; background: var(--accent-orange); }
  .brand-name {
    font-weight: 700; font-size: 27px; color: var(--brand-blue); letter-spacing: -0.3px;
  }
  .front-divider {
    position: absolute; left: 262px; top: 40px; width: 1px; height: 190px;
    background: var(--divider);
  }
  .person { position: absolute; left: 286px; top: 28px; color: var(--ink); }
  .person-name { font-size: 22px; font-weight: 700; color: var(--brand-blue); }
  .person-role { font-size: 15px; margin-top: 6px; }
  .person-address { font-size: 15px; line-height: 22px; margin-top: 40px; }
  .front-rule {
    position: absolute; left: 0; right: 0; top: 238px; height: 3px; background: var(--accent-orange);
  }
  .contact-band {
    position: absolute; left: 0; right: 0; top: 248px; bottom: 0;
    background: linear-gradient(180deg, var(--band-blue), var(--band-deep));
    color: var(--white); font-size: 13px; font-weight: 500;
    padding: 14px 0 0 44px; line-height: 24px;
  }
  .contact-band .sep { margin: 0 8px; }

  /* Back */
  .card-back {
    left: 636px; width: 510px;
    background: radial-gradient(ellipse at 50% 40%, var(--back-light), var(--back-dark) 80%);
    color: var(--white);
  }
  .back-brand {
    position: absolute; left: 0; right: 0; top: 0; height: 235px;
    display: flex; align-items: center; justify-content: center; gap: 12px;
  }
  .back-brand .brand-name { color: var(--white); font-size: 34px; }
  .back-brand .brand-dot { width: 26px; height: 26px; }
  .back-address {
    position: absolute; left: 0; right: 0; top: 256px;
    text-align: center; font-size: 15px; line-height: 26px;
  }
</style>
</head>
<body>
<main class="canvas">
  <section class="card card-front" aria-label="Card front">
    <div class="front-brand">
      <span class="brand-dot"></span>
      <span class="brand-name">Lumora Fabrix</span>
    </div>
    <div class="front-divider"></div>
    <div class="person">
      <p class="person-name">Ravi Kapoorji</p>
      <p class="person-role">Business Manager</p>
      <p class="person-address">
        117, Neel Kamal Residency<br>
        Chandan Path, Moti Nagar<br>
        Jaipur - 302049<br>
        Rajasthan , India
      </p>
    </div>
    <div class="front-rule"></div>
    <div class="contact-band">
      <p>Cell : +91 90000 41327<span class="sep">|</span>Email : ravi.kapoorji@lumora-fabrix.example</p>
      <p>Web : www.lumora-fabrix.example</p>
    </div>
  </section>

  <section class="card card-back" aria-label="Card back">
    <div class="back-brand">
      <span class="brand-dot"></span>
      <span class="brand-name">Lumora Fabrix</span>
    </div>
    <div class="back-address">
      <p>117, Neel Kamal Residency, Chandan Path, Moti Nagar</p>
      <p>Jaipur - 302049, Rajasthan , India</p>
    </div>
  </section>
</main>
</body>
</html>
```